Brivance Healthcare International Corporate & Brand Showcase

Brivance Healthcare is a new Healthcare company, specialising in the Preventative care in the Healthcare cycle. Brivance provides a range of products in different categories across bacterial and virus infection prevention and control.

Product Categories:
- Anti-Bacterial Hand Cleansing Gels
- Anti-Bacterial Hand Sanitizers
- Hypochlorous Anti-Bacterial Disinfectant (Non-alcohol based)
- Automatic Air Disinfection Spray Humidifiers
- Infra-red Hand Thermometers
- Anti-Bacterial Multi-Purpose Disinfection Spray

Each Category will require its own page description with product visuals and for the Spray Humidifiers - video clips.

The Website will require the following pages:
Home Page
About Us
Our Brands
- Moravel
- Brivance
- Tessik-bio (please refer to www.Tessik-bio.example for product information and product range - Brivance Healthcare will sell these products)
Product Information
- by category
Specific Usage occasions
Regulatory Certification
Contact Us/ Enquiry (Name (1st/2nd)/ Company name/ Contact email/ contact no/ Products of interest/...)
Shopify Order Form with auto-payment (Is this a separate webpage/site?!)

The Brand and Corporate personality will be Health & Personal Care oriented . (See existing pack designs attached)
Key words are: Kind, caring, cleansing, fresh, germ-free, anti-bacterial, professional, serene, GLC and KRT Approved.

Colours: Green/ blue, white, silver (see pack designs)

Lets use landscape imagery to style the Corporate personality (and not just brand pack shots).

The Banner strip on each page should have these words:
Enquiries
+44 (0)987 654 3210
sales@brivancehealthcare.example

Many thanks
Best wishes
Derek.
Updates

Need extra days to review

Target Market(s)

Corporate market
Retailers
Hotels & Leisure sectors
Consumers

Font styles to use
Sans Serif

Colors
9bcb3c
fbed22
33a6d7
e34197
876aae
0555a3

Requirements
Must have
• Strapline :
For Brivance Protection

Home Page
About Us
Our Brands
- Moravel
- Brivance
Product Information
- by category
Specific Usage occasions
Regulatory Certification

Enquiries
+44 (0)987 654 3210
Nice to have
• Colours: Green/ blue, white, silver (see pack designs)
Landscape imagery/ uplifting

```html
<!DOCTYPE html>
<html lang="en">
<head>
<meta charset="utf-8">
<title>Brivance Healthcare – Usage Occasions</title>
<link rel="stylesheet" href="https://fonts.googleapis.com/css2?family=Poppins:wght@700;800&family=Lato:wght@300;400;700&family=Roboto:wght@400;500&display=swap">
<style>
:root{
  --green:#3fae29;
  --green-dark:#2c8a18;
  --green-title:#2f8a1a;
  --blue:#2a4fc4;
  --blue-light:#e8ecf8;
  --field-border:#a6b0dc;
  --dark:#222222;
  --white:#ffffff;
  --text:#2b2b2b;
}
*{margin:0;padding:0;box-sizing:border-box}
html,body{width:1200px;height:2280px;overflow:hidden}
body{position:relative;background:var(--white);font-family:'Lato',sans-serif;color:var(--text)}
.abs{position:absolute}

/* top bar */
.top-bar{left:0;top:0;width:1200px;height:50px;background:var(--green)}
.top-contact{top:14px;display:flex;align-items:center;gap:10px;color:var(--white);font-family:'Roboto',sans-serif;font-size:17px;letter-spacing:2px;white-space:nowrap}
.top-contact svg{width:22px;height:22px}
.enquire-btn{left:966px;top:7px;width:134px;height:35px;border-radius:18px;background:var(--white);color:var(--blue);font-family:'Roboto',sans-serif;font-weight:500;font-size:15px;display:flex;align-items:center;justify-content:center;box-shadow:0 2px 4px rgba(0,0,0,.25)}

/* header */
.header{left:0;top:50px;width:1200px;height:118px;background:var(--white)}
.brand-tab{left:97px;top:50px;width:248px;height:172px;background:var(--white);z-index:3;display:flex;flex-direction:column;align-items:center;justify-content:center;padding-bottom:34px}
.brand-tab::before{content:"";position:absolute;left:28px;top:0;width:188px;height:172px;background:var(--white);z-index:-1}
.brand-name{font-family:'Lato',sans-serif;font-weight:400;font-size:54px;line-height:1;color:var(--green);white-space:nowrap}
.brand-strap{font-family:'Lato',sans-serif;font-size:10px;letter-spacing:2.5px;color:var(--green);margin-top:4px;white-space:nowrap}
.main-nav{left:387px;top:95px;display:flex;gap:20px;font-family:'Roboto',sans-serif;font-size:19px;color:var(--blue);white-space:nowrap}
.search-icon{left:1076px;top:96px;width:26px;height:26px}

/* hero */
.hero{left:0;top:168px;width:1200px;height:400px;background:radial-gradient(ellipse at 55% 20%,#eaf7b8 0%,#b7df57 35%,#78bd2a 65%,#4e9a1c 100%)}
.hero-title{left:0;top:255px;width:1200px;text-align:center;font-family:'Poppins',sans-serif;font-weight:800;font-size:45px;color:var(--green-title)}
.swoosh{left:0;top:0;width:1200px;height:2280px;pointer-events:none}

/* occasions */
.monitor{width:314px;height:206px;background:#151515;border-radius:4px;box-shadow:0 14px 14px -8px rgba(0,0,0,.45)}
.monitor::before{content:"";position:absolute;left:80px;top:0;width:234px;height:14px;background:linear-gradient(90deg,#555,#bbb 60%,#999);clip-path:polygon(0 0,100% 0,100% 100%,4% 100%)}
.screen{position:absolute;left:16px;top:15px;width:284px;height:175px;background:var(--white);display:flex;align-items:center;justify-content:center}
.occasion-icon{width:180px;height:148px;color:var(--blue)}
.power-dot{position:absolute;left:152px;top:194px;width:8px;height:8px;border:1px solid #888;border-radius:50%}

/* contact */
.contact-card{left:97px;top:1165px;width:1005px;height:527px;background:var(--white);box-shadow:0 0 10px rgba(0,0,0,.12)}
.touch-panel{left:97px;top:1165px;width:411px;height:527px;background:linear-gradient(135deg,#2b8f17,#4db531)}
.touch-title{left:97px;top:1398px;width:411px;text-align:center;font-family:'Poppins',sans-serif;font-weight:800;font-size:44px;color:var(--white);white-space:nowrap}
.touch-text{left:97px;top:1463px;width:411px;text-align:center;font-size:18px;line-height:24px;color:var(--white)}
.form-title{left:542px;top:1182px;font-family:'Poppins',sans-serif;font-weight:800;font-size:26px;color:var(--blue);letter-spacing:.3px;white-space:nowrap}
.field-label{font-size:14px;color:var(--text)}
.field{background:linear-gradient(180deg,#fff,var(--blue-light));border:1px solid var(--field-border)}
.check-grid{left:542px;top:1381px;width:521px;height:55px;border:1px solid var(--field-border);display:grid;grid-template-columns:176px 176px 1fr;padding:6px 16px;row-gap:4px;font-size:14px;color:#8f9bd6}
.check-grid span{display:flex;align-items:center;gap:10px}
.check-grid i{width:13px;height:13px;border:1px solid #9aa4cf;display:inline-block}
.submit-btn{left:540px;top:1622px;width:138px;height:50px;border-radius:25px;background:var(--blue);color:var(--white);font-family:'Lato',sans-serif;font-weight:700;font-size:17px;display:flex;align-items:center;justify-content:center}

/* footer */
.footer-brand{left:450px;top:1935px;width:300px;display:flex;flex-direction:column;align-items:center}
.footer-brand .brand-name{font-size:60px}
.footer-brand .brand-strap{font-size:11px}
.footer-info{left:0;top:2092px;width:1200px;text-align:center;font-size:19px;color:var(--white)}
.footer-info em{font-style:normal;color:var(--green)}
.socials{left:0;top:2150px;width:1200px;display:flex;justify-content:center;gap:22px}
.social{width:51px;height:51px;border-radius:50%;background:var(--green)}
.copyright{left:0;top:2226px;width:1200px;text-align:center;font-size:14px;color:var(--white)}
</style>
</head>
<body>

<div class="abs top-bar"></div>
<div class="abs top-contact" style="left:98px">
  <svg viewBox="0 0 24 24" fill="none" stroke="#fff" stroke-width="2"><path d="M5 3l4 1 1 4-2 2a11 11 0 006 6l2-2 4 1 1 4-3 2C10 21 3 14 3 6z"/></svg>
  <span>(555) 0147-82300</span>
</div>
<div class="abs top-contact" style="left:318px">
  <svg viewBox="0 0 24 24" fill="none" stroke="#fff" stroke-width="2"><rect x="2" y="5" width="20" height="14"/><path d="M2 5l10 8 10-8"/></svg>
  <span>INFO@BRIVANCEMAIL.EXAMPLE</span>
</div>
<div class="abs enquire-btn">ENQUIRE NOW</div>

<div class="abs header"></div>
<div class="abs brand-tab">
  <div class="brand-name">Brivance</div>
  <div class="brand-strap">FOR BRIVANCE PROTECTION</div>
</div>
<nav class="abs main-nav">
  <span>HOME</span><span>ABOUT US</span><span>OUR PRODUCTS</span><span>OUR BRANDS</span><span>MEDIA</span><span>CONTACT US</span>
</nav>
<svg class="abs search-icon" viewBox="0 0 26 26" fill="none" stroke="#aaa" stroke-width="2"><circle cx="11" cy="11" r="8"/><path d="M17 17l7 7"/></svg>

<div class="abs hero" role="img" aria-label="Fresh green leaves in soft sunlight"></div>
<h1 class="abs hero-title">Ideal For Usage For All These Occasions</h1>

<svg class="abs swoosh" viewBox="0 0 1200 2280">
  <path d="M0,565 C150,440 330,378 520,395 C720,413 880,480 1040,470 C1120,464 1170,425 1200,385 L1200,575 L0,575 Z" fill="#fff"/>
  <path d="M0,520 C140,425 300,370 460,372 C640,376 800,450 980,465 C1090,472 1160,440 1200,400 L1200,385 C1170,425 1120,464 1040,470 C880,480 720,413 520,395 C330,378 150,440 0,565 Z" fill="#3fae29"/>
  <path d="M0,470 C120,405 280,375 460,388" stroke="#fff" stroke-width="4" fill="none"/>
  <path d="M0,1665 C120,1770 300,1820 520,1835" stroke="#3fae29" stroke-width="16" fill="none"/>
  <path d="M0,1790 C300,1870 600,1830 850,1775 C1000,1745 1130,1770 1200,1840 L1200,2280 L0,2280 Z" fill="#222"/>
  <path d="M0,1770 C300,1850 600,1812 850,1757 C1000,1727 1130,1752 1200,1822 L1200,1840 C1130,1770 1000,1745 850,1775 C600,1830 300,1870 0,1790 Z" fill="#3fae29"/>
  <path d="M0,1740 C180,1810 330,1840 460,1845" stroke="#fff" stroke-width="4" fill="none"/>
</svg>

<!-- Home -->
<div class="abs monitor" style="left:99px;top:562px"><div class="screen">
  <svg class="occasion-icon" viewBox="0 0 170 140" role="img" aria-label="Home">
    <rect x="112" y="20" width="16" height="34" fill="currentColor"/>
    <path d="M22 74 L85 20 L148 74" fill="none" stroke="currentColor" stroke-width="14" stroke-linecap="round" stroke-linejoin="round"/>
    <path d="M46 72 L85 38 L124 72 V132 H98 V100 H72 V132 H46 Z" fill="currentColor"/>
  </svg>
</div><div class="power-dot"></div></div>

<!-- Office -->
<div class="abs monitor" style="left:442px;top:562px"><div class="screen">
  <svg class="occasion-icon" viewBox="0 0 170 140" role="img" aria-label="Office building">
    <rect x="60" y="8" width="50" height="122" fill="currentColor"/>
    <rect x="34" y="36" width="28" height="94" fill="currentColor"/>
    <rect x="108" y="36" width="28" height="94" fill="currentColor"/>
    <g fill="#fff">
      <rect x="67" y="18" width="9" height="10"/><rect x="81" y="18" width="9" height="10"/><rect x="95" y="18" width="9" height="10"/>
      <rect x="67" y="36" width="9" height="10"/><rect x="81" y="36" width="9" height="10"/><rect x="95" y="36" width="9" height="10"/>
      <rect x="67" y="54" width="9" height="10"/><rect x="81" y="54" width="9" height="10"/><rect x="95" y="54" width="9" height="10"/>
      <rect x="67" y="72" width="9" height="10"/><rect x="81" y="72" width="9" height="10"/><rect x="95" y="72" width="9" height="10"/>
      <rect x="76" y="98" width="18" height="32"/>
      <rect x="40" y="46" width="16" height="3"/><rect x="40" y="56" width="16" height="3"/><rect x="40" y="66" width="16" height="3"/><rect x="40" y="76" width="16" height="3"/><rect x="40" y="86" width="16" height="3"/><rect x="40" y="96" width="16" height="3"/><rect x="40" y="106" width="16" height="3"/><rect x="40" y="116" width="16" height="3"/>
      <rect x="114" y="46" width="16" height="3"/><rect x="114" y="56" width="16" height="3"/><rect x="114" y="66" width="16" height="3"/><rect x="114" y="76" width="16" height="3"/><rect x="114" y="86" width="16" height="3"/><rect x="114" y="96" width="16" height="3"/><rect x="114" y="106" width="16" height="3"/><rect x="114" y="116" width="16" height="3"/>
    </g>
    <rect x="24" y="132" width="122" height="5" fill="currentColor"/>
  </svg>
</div><div class="power-dot"></div></div>

<!-- Gym -->
<div class="abs monitor" style="left:783px;top:562px"><div class="screen">
  <svg class="occasion-icon" viewBox="0 0 170 140" role="img" aria-label="Gym exercise bike">
    <g fill="none" stroke="currentColor" stroke-width="9" stroke-linecap="round">
      <path d="M62 130 L70 64"/>
      <path d="M70 64 L102 100"/>
      <path d="M102 100 L116 36"/>
      <path d="M112 34 L134 24"/>
    </g>
    <rect x="50" y="54" width="36" height="10" rx="5" fill="currentColor"/>
    <circle cx="104" cy="104" r="24" fill="currentColor"/>
    <circle cx="104" cy="104" r="9" fill="#fff"/>
    <rect x="34" y="128" width="104" height="7" rx="3.5" fill="currentColor"/>
  </svg>
</div><div class="power-dot"></div></div>

<!-- School -->
<div class="abs monitor" style="left:99px;top:836px"><div class="screen">
  <svg class="occasion-icon" viewBox="0 0 170 140" role="img" aria-label="Graduation cap for schools">
    <path d="M46 62 V100 Q85 124 124 100 V62 L85 78 Z" fill="currentColor"/>
    <polygon points="6,48 85,18 164,48 85,78" fill="currentColor"/>
    <path d="M85 46 L142 56 V104" fill="none" stroke="#fff" stroke-width="3"/>
    <path d="M85 46 L142 56 V104" fill="none" stroke="currentColor" stroke-width="5" transform="translate(0,4)"/>
    <polygon points="140,104 152,104 146,128" fill="currentColor"/>
  </svg>
</div><div class="power-dot"></div></div>

<!-- Travel -->
<div class="abs monitor" style="left:442px;top:836px"><div class="screen">
  <svg class="occasion-icon" viewBox="0 0 170 140" role="img" aria-label="Globe and aeroplane for travel">
    <circle cx="72" cy="74" r="52" fill="currentColor"/>
    <g fill="none" stroke="#fff" stroke-width="3">
      <ellipse cx="72" cy="74" rx="22" ry="52"/>
      <path d="M20 74 H124"/>
      <path d="M28 48 Q72 58 116 48"/>
      <path d="M28 100 Q72 90 116 100"/>
    </g>
    <path d="M12 112 Q80 118 150 46" fill="none" stroke="#fff" stroke-width="12"/>
    <path d="M12 112 Q80 118 150 46" fill="none" stroke="currentColor" stroke-width="6" stroke-linecap="round"/>
    <g transform="rotate(-35 132 38)" fill="currentColor" stroke="#fff" stroke-width="2">
      <rect x="104" y="33" width="56" height="10" rx="5"/>
      <polygon points="126,38 116,14 126,14 146,38 126,62 116,62"/>
      <polygon points="106,38 100,26 106,26 114,38 106,50 100,50"/>
    </g>
  </svg>
</div><div class="power-dot"></div></div>

<!-- Stadium -->
<div class="abs monitor" style="left:783px;top:836px"><div class="screen">
  <svg class="occasion-icon" viewBox="0 0 170 140" role="img" aria-label="Stadium for events">
    <path d="M8 44 V104 Q85 136 162 104 V44 Q85 80 8 44 Z" fill="currentColor"/>
    <ellipse cx="85" cy="40" rx="74" ry="24" fill="none" stroke="currentColor" stroke-width="9"/>
    <g stroke="currentColor" stroke-width="4">
      <path d="M40 24 L52 52"/><path d="M62 18 L68 56"/><path d="M85 16 V58"/><path d="M108 18 L102 56"/><path d="M130 24 L118 52"/>
    </g>
    <g fill="none" stroke="#fff" stroke-width="3">
      <path d="M8 70 Q85 102 162 70"/>
      <path d="M8 88 Q85 120 162 88"/>
      <path d="M34 64 V114"/><path d="M60 70 V122"/><path d="M110 70 V122"/><path d="M136 64 V114"/>
    </g>
    <rect x="68" y="96" width="34" height="28" fill="#fff"/>
    <rect x="76" y="104" width="18" height="14" fill="currentColor"/>
  </svg>
</div><div class="power-dot"></div></div>

<div class="abs contact-card"></div>
<div class="abs touch-panel"></div>
<div class="abs touch-title">GET IN TOUCH!</div>
<p class="abs touch-text">Brivance Healthcare.<br>For your health, protection and wellbeing.</p>

<h2 class="abs form-title">CONTACT BRIVANCE TODAY</h2>
<label class="abs field-label" style="left:543px;top:1222px">First Name</label>
<label class="abs field-label" style="left:827px;top:1222px">Last Name</label>
<div class="abs field" style="left:542px;top:1246px;width:241px;height:34px"></div>
<div class="abs field" style="left:827px;top:1246px;width:236px;height:34px"></div>
<label class="abs field-label" style="left:543px;top:1290px">Company name</label>
<label class="abs field-label" style="left:827px;top:1290px">Contact email</label>
<div class="abs field" style="left:542px;top:1315px;width:241px;height:34px"></div>
<div class="abs field" style="left:827px;top:1315px;width:236px;height:34px"></div>
<label class="abs field-label" style="left:543px;top:1358px">Product categories</label>
<div class="abs check-grid">
  <span><i></i>Product One</span><span><i></i>Product Two</span><span><i></i>Product Three</span>
  <span><i></i>Product Four</span><span><i></i>Product Five</span><span><i></i>Product six</span>
</div>
<label class="abs field-label" style="left:543px;top:1446px">Contact no</label>
<label class="abs field-label" style="left:827px;top:1446px">Products of interest</label>
<div class="abs field" style="left:542px;top:1470px;width:241px;height:34px"></div>
<div class="abs field" style="left:827px;top:1470px;width:236px;height:34px"></div>
<label class="abs field-label" style="left:543px;top:1511px">Enquiry</label>
<div class="abs field" style="left:542px;top:1537px;width:521px;height:75px"></div>
<div class="abs submit-btn">SUBMIT</div>

<div class="abs footer-brand">
  <div class="brand-name">Brivance</div>
  <div class="brand-strap">FOR BRIVANCE PROTECTION</div>
</div>
<p class="abs footer-info"><em>Address:</em> Harwick, TX 77000, USA &nbsp;|&nbsp; <em>Phone:</em> 5550147823 &nbsp;|&nbsp; <em>Email:</em> info@brivancemail.example</p>
<div class="abs socials">
  <span class="social" role="img" aria-label="Social link 1"></span>
  <span class="social" role="img" aria-label="Social link 2"></span>
  <span class="social" role="img" aria-label="Social link 3"></span>
  <span class="social" role="img" aria-label="Social link 4"></span>
  <span class="social" role="img" aria-label="Social link 5"></span>
</div>
<p class="abs copyright">Brivance Protection &nbsp;| All Rights Reserved &nbsp;© 2020</p>

</body>
</html>
```